Website design for luxury private hair salon

I'm looking for someone to use my Logo and build me a website for my webpage www.lunetresses.com.au (You can have a look at it as it has every detail I need included on it already), however I want a fresh new appearance and it to look and feel super stylish.

I am thinking colours in black, with silver or white, beautiful hair images like the ones you'll see on the current webpage - the price list as per what you already see.

I will include a copy of my biz card on here, so you can see the feel of the card, and design a website with a similar feel. It is matt black with a foil silver.

Modern, but classic and fresh. I will also need you to be able to publish it to my URL for me as I have no idea how to do this. I need it up and running pronto!

The website will need to be able to be read clearly on all devices incluing smart phones and ipads. The URL is currently registered and hosted by Nimbo Vault

Thinking a Home Page - large logo etc and write up on who and what we offer
Services/Price List page - as per the price list on my current webpage
Contact Page - with a built in contact form.

Target Market(s)

Middle aged, fashionable, stylish women and men who enjoy luxury hair care and styling in an upmarket location.

Industry/Entity Type

Hair And Beauty

Number of Pages Required

3 page

Font styles to use
Other font styles liked:
• see my images for my current logo

Colors
000000
b2b2b2
a54499

Requirements
Must have
• Style
• Fast turnaround
• Be viewable on all devices, PC, ipads, smart phones
• Designer able to upload it so its a running website for me to my URL
Nice to have
• Just a really feminine, stylish website which is easy to read and shows some beautiful images of perfect hair
Should not have
• Browns, reds or orange colours.

```html
<!DOCTYPE html>
<html lang="en">
<head>
<meta charset="utf-8">
<title>Lune hair &amp; body</title>
<link rel="stylesheet" href="https://fonts.googleapis.com/css2?family=Lato:wght@300;400&family=Montserrat:wght@500&display=swap">
<style>
  :root {
    --ink: #111111;
    --paper: #ffffff;
    --silver: #d6d6d6;
    --nav-text: #f2f2f2;
    --body-text: #222222;
    --hair-light: #efe4bf;
    --hair-mid: #c9b27a;
    --hair-deep: #6e5c3a;
  }
  * { margin: 0; padding: 0; box-sizing: border-box; }
  html, body {
    width: 1200px;
    height: 1046px;
    overflow: hidden;
    background: var(--paper);
  }
  .page {
    position: relative;
    width: 1200px;
    height: 1046px;
    background: var(--paper);
    font-family: "Lato", sans-serif;
  }
  .top-band {
    position: absolute;
    left: 0; top: 0;
    width: 1200px; height: 107px;
    background: var(--ink);
  }
  .hero-photo {
    position: absolute;
    left: 0; top: 107px;
    width: 496px; height: 789px;
    background:
      radial-gradient(ellipse at 30% 20%, var(--hair-light) 0%, transparent 60%),
      linear-gradient(160deg, var(--hair-light) 0%, var(--hair-mid) 55%, var(--hair-deep) 78%, var(--hair-light) 100%);
  }
  .brand-panel {
    position: absolute;
    left: 496px; top: 107px;
    width: 704px; height: 459px;
    background: var(--ink);
  }
  .main-nav {
    position: absolute;
    right: 34px; top: 12px;
    display: flex;
    gap: 22px;
  }
  .main-nav a {
    color: var(--nav-text);
    text-decoration: none;
    font-size: 16px;
    font-weight: 300;
    padding-bottom: 8px;
  }
  .main-nav a.is-active { border-bottom: 2px solid var(--nav-text); }
  .brand-name {
    position: absolute;
    left: 0; right: 0; top: 80px;
    text-align: center;
    color: var(--silver);
    font-weight: 300;
    line-height: 1;
  }
  .brand-name .brand-word {
    display: block;
    font-size: 170px;
    letter-spacing: 4px;
  }
  .brand-name .brand-sub {
    display: block;
    margin-top: 24px;
    font-size: 46px;
    letter-spacing: 10px;
  }
  .intro {
    position: absolute;
    left: 567px; top: 604px;
    width: 600px;
  }
  .intro-quote {
    font-size: 29px;
    font-weight: 300;
    line-height: 42.7px;
    color: var(--body-text);
  }
  .intro-signature {
    margin-top: 20px;
    font-family: "Montserrat", sans-serif;
    font-weight: 500;
    font-size: 31px;
    color: var(--ink);
  }
</style>
</head>
<body>
<div class="page">
  <div class="top-band"></div>
  <div class="hero-photo" role="img" aria-label="Portrait of a woman with long, sunlit blonde hair in a golden field"></div>
  <header class="brand-panel">
    <nav class="main-nav">
      <a href="#" class="is-active">Home</a>
      <a href="#">Price List</a>
    </nav>
    <h1 class="brand-name">
      <span class="brand-word">Lune</span>
      <span class="brand-sub">hair &amp; body</span>
    </h1>
  </header>
  <section class="intro">
    <p class="intro-quote">"We pride ourselves on being able to<br>offer a private salon experience to our<br>clients in the exclusive suburb of<br>Marlow Heights, where your hair design and<br>colouring needs will be met with years of<br>experience and current industry training<br>and knowledge".</p>
    <p class="intro-signature">- The Lune Team -</p>
  </section>
</div>
</body>
</html>
```